Business card for partnership

Plumbing and hvac company needing a minimal business card. We already have a logo i would like the front of the card just the logo and the back have all info.

Target Market(s)

Commercial facilities

Industry/Entity Type

Plumbing hvac

Contact Information for Business Card

We would like it double sided. Logo big and bold on the front and out info on the back. Our info on back would be name and position phone, email, and location

```html
<!DOCTYPE html>
<html lang="en">
<head>
<meta charset="utf-8">
<title>Ridgeline Mechanical – Business Card</title>
<link rel="stylesheet" href="https://fonts.googleapis.com/css2?family=Lato:wght@400;700;900&display=swap">
<style>
  :root {
    --page-bg: #141416;
    --card-bg: #2e2f37;
    --accent: #f28a3a;
    --accent-deep: #e4632f;
    --ink-light: #f2f2f4;
    --ink-soft: #d9d9de;
  }
  * { box-sizing: border-box; margin: 0; padding: 0; }
  html, body {
    width: 1200px;
    height: 1122px;
    overflow: hidden;
    background: var(--page-bg);
    font-family: "Lato", sans-serif;
  }
  .canvas {
    position: relative;
    width: 1200px;
    height: 1122px;
  }
  .card {
    position: absolute;
    left: 250px;
    width: 700px;
    height: 400px;
    background: var(--card-bg);
    border-radius: 28px;
    overflow: hidden;
  }
  .card--info { top: 110px; }
  .card--brand { top: 612px; }

  /* Info side */
  .info-mark {
    position: absolute;
    left: 48px;
    top: 50%;
    transform: translateY(-50%);
    display: flex;
    align-items: center;
    gap: 14px;
  }
  .info-mark__square {
    width: 56px;
    height: 56px;
    background: var(--accent);
    border-radius: 4px;
  }
  .info-mark__name {
    color: var(--accent);
    font-weight: 900;
    font-size: 22px;
    letter-spacing: 1px;
    line-height: 1.15;
    text-transform: uppercase;
  }
  .contact {
    position: absolute;
    right: 48px;
    top: 78px;
    text-align: right;
  }
  .contact__name {
    color: var(--accent);
    font-weight: 700;
    font-size: 32px;
    letter-spacing: 1px;
    text-transform: uppercase;
    line-height: 1;
  }
  .contact__role {
    color: var(--ink-light);
    font-size: 19px;
    font-weight: 700;
    letter-spacing: 0.5px;
    margin-top: 6px;
    margin-right: 0;
  }
  .contact__list {
    list-style: none;
    margin-top: 26px;
  }
  .contact__item {
    display: flex;
    justify-content: flex-end;
    align-items: flex-start;
    gap: 12px;
    color: var(--ink-soft);
    font-size: 17px;
    letter-spacing: 0.6px;
    line-height: 1.4;
    margin-bottom: 4px;
  }
  .contact__icon {
    width: 16px;
    height: 16px;
    flex: 0 0 16px;
    margin-top: 4px;
    fill: var(--accent);
  }

  /* Brand side */
  .brand {
    position: absolute;
    inset: 0;
    display: flex;
    align-items: center;
    justify-content: center;
    gap: 22px;
  }
  .brand__square {
    width: 70px;
    height: 70px;
    background: var(--accent);
    border-radius: 6px;
  }
  .brand__name {
    color: var(--ink-light);
    font-weight: 900;
    font-size: 44px;
    letter-spacing: 3px;
    line-height: 1.05;
    text-transform: uppercase;
  }
</style>
</head>
<body>
<main class="canvas">
  <section class="card card--info" aria-label="Card back with contact details">
    <div class="info-mark">
      <span class="info-mark__square"></span>
      <span class="info-mark__name">Ridgeline<br>Mechanical</span>
    </div>
    <div class="contact">
      <h1 class="contact__name">Dale Harrow</h1>
      <p class="contact__role">Founder &amp; CEO</p>
      <ul class="contact__list">
        <li class="contact__item">
          <span>Your Address, City<br>State, Zip 1235</span>
          <svg class="contact__icon" viewBox="0 0 16 16" aria-hidden="true"><path d="M8 0a5.5 5.5 0 0 0-5.5 5.5C2.5 10 8 16 8 16s5.5-6 5.5-10.5A5.5 5.5 0 0 0 8 0zm0 8a2.5 2.5 0 1 1 0-5 2.5 2.5 0 0 1 0 5z"/></svg>
        </li>
        <li class="contact__item">
          <span>(123) 456-7890</span>
          <svg class="contact__icon" viewBox="0 0 16 16" aria-hidden="true"><path d="M3.6 1h2.3l1.2 3.4-1.6 1.3a9 9 0 0 0 4.8 4.8l1.3-1.6 3.4 1.2v2.3c0 .9-.7 1.6-1.6 1.6C6.9 14 2 9.1 2 2.6 2 1.7 2.7 1 3.6 1z"/></svg>
        </li>
        <li class="contact__item">
          <span>info@RidgelineMech.com</span>
          <svg class="contact__icon" viewBox="0 0 16 16" aria-hidden="true"><path d="M1 3h14v10H1zm1.5 1.2L8 8.6l5.5-4.4z"/></svg>
        </li>
        <li class="contact__item">
          <span>RidgelineMech.com</span>
          <svg class="contact__icon" viewBox="0 0 16 16" aria-hidden="true"><path d="M8 1a7 7 0 1 0 0 14A7 7 0 0 0 8 1zm0 1.5c.8 0 1.7 1.6 2 4H6c.3-2.4 1.2-4 2-4zM2.6 7.5h2c0-1.6.3-3 .8-3.9A5.5 5.5 0 0 0 2.6 7.5zm0 1a5.5 5.5 0 0 0 2.8 3.9c-.5-.9-.8-2.3-.8-3.9zm3.4 0h4c-.2 2.4-1.1 4-2 4s-1.8-1.6-2-4zm5.4 0c0 1.6-.3 3-.8 3.9a5.5 5.5 0 0 0 2.8-3.9zm2-1a5.5 5.5 0 0 0-2.8-3.9c.5.9.8 2.3.8 3.9z"/></svg>
        </li>
      </ul>
    </div>
  </section>

  <section class="card card--brand" aria-label="Card front with company name">
    <div class="brand">
      <span class="brand__square"></span>
      <span class="brand__name">Ridgeline<br>Mechanical</span>
    </div>
  </section>
</main>
</body>
</html>
```